Webdesign für lokalen Dart-Shop
Zielgruppe
Wir sind ein lokaler Dart-Shop in Hamburg, welcher in Norddeutschland sehr beliebt ist und bundesweit das Größte Angebot bietet. Durch unseren Online-Shop möchte wir unseren Radius erweitern.
Zielgruppe: Dart Anfänger, Fortgeschrittene sowie Vereine und Unternehmen
Aufgabenstellung
In jedem Fall das Haupt-Element unseres Logo´s, einer Dart-Scheibe.

```html
<!DOCTYPE html>
<html lang="de">
<head>
<meta charset="utf-8">
<title>Wurfpunkt Hamburg – Dartshop</title>
<link rel="stylesheet" href="https://fonts.googleapis.com/css2?family=Roboto:wght@400;700&display=swap">
<style>
  :root {
    --black: #000000;
    --red: #bf1a1a;
    --red-dark: #a81212;
    --red-text: #d4141b;
    --white: #ffffff;
    --ink: #343a40;
    --body: #222222;
    --photo-dark: #151515;
    --photo-mid: #4a4a4a;
    --photo-light: #9a9a9a;
  }
  * { margin: 0; padding: 0; box-sizing: border-box; }
  html, body {
    width: 1200px; height: 675px; overflow: hidden;
    background: var(--white);
    font-family: "Roboto", Arial, sans-serif;
  }
  .site { position: relative; width: 1200px; height: 675px; }
  .site-header {
    position: absolute; left: 0; top: 0; width: 1200px; height: 104px;
    background: var(--black); z-index: 2;
  }
  .brand {
    position: absolute; left: 150px; top: 24px;
    display: flex; align-items: center; gap: 10px;
    color: var(--white); font-weight: 700; font-size: 17px; letter-spacing: 0.5px;
  }
  .brand-dot {
    width: 44px; height: 44px; border-radius: 50%;
    border: 3px solid var(--white);
  }
  .main-nav {
    position: absolute; top: 82px; left: 490px;
    display: flex; gap: 56px;
  }
  .main-nav a {
    color: var(--white); text-decoration: none; font-size: 12px; font-weight: 700;
  }
  .hero { position: absolute; left: 0; top: 0; width: 1200px; height: 500px; z-index: 1; }
  .intro { position: absolute; left: 120px; top: 520px; width: 960px; }
  .intro h1 {
    color: var(--ink); font-size: 36px; font-weight: 700; letter-spacing: 0.2px;
  }
  .intro p {
    margin-top: 16px; color: var(--body); font-size: 11.5px; line-height: 1.6; width: 720px;
  }
  .support {
    position: absolute; left: 0; width: 1200px; top: 638px; text-align: center;
    color: var(--red-text); font-size: 17px; font-weight: 700;
  }
</style>
</head>
<body>
<div class="site">
  <header class="site-header">
    <div class="brand"><span class="brand-dot"></span>Wurfpunkt Hamburg</div>
    <nav class="main-nav">
      <a href="#">Home</a>
      <a href="#">Shop</a>
      <a href="#">News</a>
    </nav>
  </header>

  <svg class="hero" viewBox="0 0 1200 500" width="1200" height="500">
    <defs>
      <linearGradient id="photoTone" x1="0" y1="0" x2="1" y2="0.4">
        <stop offset="0" stop-color="var(--photo-light)"/>
        <stop offset="0.35" stop-color="var(--photo-mid)"/>
        <stop offset="0.7" stop-color="var(--photo-dark)"/>
        <stop offset="1" stop-color="var(--photo-mid)"/>
      </linearGradient>
      <linearGradient id="photoFade" x1="0" y1="0" x2="1" y2="0">
        <stop offset="0" stop-color="#000" stop-opacity="1"/>
        <stop offset="0.12" stop-color="#000" stop-opacity="0"/>
      </linearGradient>
    </defs>
    <rect x="0" y="0" width="1200" height="500" fill="var(--black)"/>
    <g role="img" aria-label="Schwarz-weiß Foto: Spieler zielt mit einem Dartpfeil">
      <rect x="400" y="104" width="800" height="396" fill="url(#photoTone)"/>
      <rect x="400" y="104" width="800" height="396" fill="url(#photoFade)"/>
    </g>
    <polygon points="0,432 640,496 1200,430 1200,500 0,500" fill="var(--red)"/>
    <polygon points="0,432 640,496 0,500" fill="var(--red-dark)" opacity="0.5"/>
  </svg>

  <section class="intro">
    <h1>Willkommen in unserem Dartshop</h1>
    <p>Wir führen eine Vielzahl an Produkten, sollte aber dennoch ein Artikel nicht dabei sein einfach eine kurze E-Mail an: info@wurfpunkt-laden.de schicken. Wir setzen uns mit Ihnen umgehend in Verbindung.</p>
  </section>

  <h2 class="support">Ihr möchtet uns gerne unterstützen?</h2>
</div>
</body>
</html>
```